Tidewell Recovery Business Card Design

Professional and clean design. The design colors should flow with the logo. Two-sided card with the website on the back which is:

www.TidewellRecovery.example.

"Specializing in Water Damage Restoration"

On the front I need the name, email, phone, and logo.

Name: Dorian Vashti
Email: Dorian@TidewellRecovery.example
Phone: 555-318-2046 for now

I only have the Preview and Thumbnail right now but should have the source files uploaded within a day or two.

Target Market(s)

Flood victims, home owners with water damage from busted pipes etc...

Industry/Entity Type

Business

Contact Information for Business Card

Name: Dorian Vashti

Font styles to use
Serif
Sans Serif

```html
<!DOCTYPE html>
<html lang="en">
<head>
<meta charset="utf-8">
<title>Tidewell Recovery Business Card</title>
<link rel="stylesheet" href="https://fonts.googleapis.com/css2?family=Cinzel:wght@400;600&family=Open+Sans:wght@400&display=swap">
<style>
  :root {
    --page: #e9e9e7;
    --card-white: #ffffff;
    --brand-blue: #2a97d4;
    --accent-blue: #56bdea;
    --ink-blue: #2a8fd0;
    --on-blue: #ffffff;
    --shadow: rgba(0,0,0,0.18);
  }
  * { margin: 0; padding: 0; box-sizing: border-box; }
  html, body { width: 1200px; height: 1000px; overflow: hidden; }
  body {
    background: var(--page);
    position: relative;
    font-family: "Open Sans", Arial, sans-serif;
  }
  .card {
    position: absolute;
    left: 230px;
    width: 740px;
    height: 420px;
    box-shadow: 0 6px 18px var(--shadow);
    overflow: hidden;
  }
  /* Back side */
  .card-back { top: 50px; background: var(--card-white); }
  .brand {
    position: absolute;
    left: 0; right: 0;
    text-align: center;
    font-family: "Cinzel", Georgia, serif;
    font-weight: 600;
  }
  .brand-mark {
    display: block;
    margin: 0 auto 14px;
    border-radius: 50%;
  }
  .card-back .brand { top: 50px; color: var(--ink-blue); }
  .card-back .brand-mark { width: 86px; height: 86px; background: var(--brand-blue); }
  .card-back .brand-name { font-size: 44px; letter-spacing: 2px; line-height: 1.1; }
  .tagline {
    position: absolute;
    top: 250px; left: 0; right: 0;
    text-align: center;
    color: var(--ink-blue);
    font-size: 17px;
    letter-spacing: 1.5px;
  }
  .web-band {
    position: absolute;
    top: 300px; left: 0; right: 0;
    height: 34px;
    background: var(--accent-blue);
    color: var(--on-blue);
    font-size: 16px;
    letter-spacing: 1px;
    line-height: 34px;
    text-align: center;
  }
  /* Front side */
  .card-front { top: 520px; background: var(--brand-blue); }
  .card-front .brand { top: 24px; color: var(--on-blue); }
  .card-front .brand-mark { width: 76px; height: 76px; background: var(--on-blue); margin-bottom: 10px; }
  .card-front .brand-name { font-size: 38px; letter-spacing: 2px; line-height: 1.1; }
  .contact-panel {
    position: absolute;
    left: 40px; right: 46px;
    top: 210px; bottom: 34px;
    background: var(--card-white);
  }
  .person-name {
    position: absolute;
    top: 22px; left: 0; right: 0;
    text-align: center;
    font-family: "Cinzel", Georgia, serif;
    font-weight: 400;
    font-size: 30px;
    color: var(--ink-blue);
    letter-spacing: 1px;
  }
  .contact-row {
    position: absolute;
    left: 0;
    display: flex;
    align-items: center;
    color: var(--ink-blue);
    font-size: 19px;
    letter-spacing: 1px;
  }
  .contact-row.email { top: 82px; }
  .contact-row.phone { top: 120px; }
  .contact-bar {
    width: 120px; height: 12px;
    background: var(--accent-blue);
  }
  .contact-badge {
    width: 30px; height: 30px;
    border-radius: 50%;
    border: 3px solid var(--accent-blue);
    background: var(--card-white);
    color: var(--ink-blue);
    font-size: 15px;
    font-weight: 400;
    display: flex; align-items: center; justify-content: center;
    margin: 0 10px 0 -2px;
  }
</style>
</head>
<body>
  <section class="card card-back" aria-label="Card back">
    <div class="brand">
      <span class="brand-mark"></span>
      <div class="brand-name">TIDEWELL RECOVERY</div>
    </div>
    <p class="tagline">"Specializing in Water Damage Restoration"</p>
    <div class="web-band">www.TidewellRecovery.example</div>
  </section>

  <section class="card card-front" aria-label="Card front">
    <div class="brand">
      <span class="brand-mark"></span>
      <div class="brand-name">TIDEWELL RECOVERY</div>
    </div>
    <div class="contact-panel">
      <h1 class="person-name">Dorian Vashti</h1>
      <div class="contact-row email">
        <span class="contact-bar"></span>
        <span class="contact-badge">M</span>
        <span>Dorian@TidewellRecovery.example</span>
      </div>
      <div class="contact-row phone">
        <span class="contact-bar"></span>
        <span class="contact-badge">E</span>
        <span>555-318-2046</span>
      </div>
    </div>
  </section>
</body>
</html>
```